Business Card Design Project

We consult with hotels on setting rates and maximizing a revenue strategy

Industry/Entity Type

Business

Contact Information for Business Card

I am not sure what I want. Our company offers high level consulting to hotels around the country but we are also laid back. I would like something that is professional but also shows the laid back side

```html
<!DOCTYPE html>
<html lang="en">
<head>
<meta charset="utf-8">
<title>Harborline – Business Card</title>
<link rel="stylesheet" href="https://fonts.googleapis.com/css2?family=Encode+Sans+Condensed:wght@600&family=Lato:ital,wght@0,400;0,700;1,400&display=swap">
<style>
  :root {
    --page: #ffffff;
    --card-top: #f3f3f5;
    --card-mid: #c8c8e0;
    --card-low: #8c8ec6;
    --card-bottom: #454d9d;
    --ink: #2b1f1c;
    --light: #ffffff;
    --teal: #5aa898;
    --teal-deep: #2f7466;
  }
  * { box-sizing: border-box; margin: 0; padding: 0; }
  html, body {
    width: 1200px; height: 511px; overflow: hidden;
    background: var(--page);
    font-family: "Lato", sans-serif;
  }
  .canvas { position: relative; width: 1200px; height: 511px; }
  .card {
    position: absolute; top: 39px; width: 562px; height: 338px;
    background: linear-gradient(180deg, var(--card-top) 0%, var(--card-top) 18%, var(--card-mid) 48%, var(--card-low) 75%, var(--card-bottom) 100%);
    overflow: hidden;
  }
  .card--front { left: 0; }
  .card--back { left: 636px; width: 564px; }

  .brand-name {
    position: absolute; color: var(--ink);
    font-weight: 700; font-size: 54px; line-height: 1;
    letter-spacing: 3px; white-space: nowrap;
  }
  .card--front .brand-name { left: 40px; top: 38px; }
  .card--back .brand-name { left: 201px; top: 132px; }

  .tagline-band { position: absolute; width: 350px; height: 39px; }
  .tagline-band svg { position: absolute; inset: 0; width: 100%; height: 100%; }
  .tagline-band path { fill: var(--ink); }
  .tagline {
    position: relative; display: block;
    font-family: "Encode Sans Condensed", sans-serif; font-weight: 600;
    font-size: 20px; line-height: 39px; color: var(--light); white-space: nowrap;
  }
  .card--front .tagline-band { left: 40px; top: 94px; }
  .card--front .tagline { padding-left: 11px; }
  .card--back .tagline-band { left: 163px; top: 189px; }
  .card--back .tagline { padding-left: 48px; }

  .star-row { position: absolute; height: 20px; }
  .star-row svg { position: absolute; top: 0; width: 19px; height: 19px; fill: var(--ink); }
  .card--front .star-row { left: 0; top: 181px; }
  .card--back .star-row { left: 0; top: 59px; }

  .bridge-art {
    position: absolute;
    background: linear-gradient(180deg, var(--teal) 0%, var(--teal-deep) 100%);
    border-radius: 4px;
    opacity: 0.85;
  }
  .card--front .bridge-art { left: 437px; top: 16px; width: 85px; height: 163px; }
  .card--back .bridge-art { left: 47px; top: 24px; width: 122px; height: 275px; }

  .holder { position: absolute; left: 53px; top: 218px; color: var(--light); }
  .holder-name { font-size: 34px; font-weight: 700; line-height: 1; }
  .holder-title { font-size: 18px; font-weight: 400; margin-top: 2px; }
  .contact {
    position: absolute; right: 42px; top: 218px;
    color: var(--light); font-style: italic; font-size: 16px;
    line-height: 20px; text-align: right; list-style: none;
  }
  .website {
    position: absolute; left: 209px; top: 253px;
    font-size: 24px; color: var(--ink);
  }
</style>
</head>
<body>
<svg width="0" height="0" style="position:absolute">
  <symbol id="star" viewBox="0 0 24 24"><polygon points="12,1 15,9 23.5,9.2 16.8,14.4 19.2,22.8 12,17.9 4.8,22.8 7.2,14.4 0.5,9.2 9,9"/></symbol>
</svg>
<main class="canvas">
  <section class="card card--front">
    <div class="brand-name">Harborline</div>
    <div class="tagline-band">
      <svg viewBox="0 0 350 39" preserveAspectRatio="none"><path d="M0 0 H292 Q334 2 350 39 H0 Z"/></svg>
      <span class="tagline">Hotel Rate Strategy Advisors</span>
    </div>
    <div class="star-row" aria-hidden="true">
      <svg style="left:49px"><use href="#star"/></svg>
      <svg style="left:133px"><use href="#star"/></svg>
      <svg style="left:220px"><use href="#star"/></svg>
      <svg style="left:314px"><use href="#star"/></svg>
      <svg style="left:404px"><use href="#star"/></svg>
    </div>
    <div class="bridge-art" role="img" aria-label="Illustration of a gothic-arched green bridge tower with a road sweeping beneath"></div>
    <div class="holder">
      <p class="holder-name">Dana Whitlock</p>
      <p class="holder-title">Regional Revenue Manager</p>
    </div>
    <ul class="contact">
      <li>Dana@HarborlineRA.com</li>
      <li>office :&nbsp; 555-014-2290</li>
      <li>fax :&nbsp; 555-014-7731</li>
    </ul>
  </section>
  <section class="card card--back">
    <div class="bridge-art" role="img" aria-label="Large illustration of a gothic-arched green bridge tower with a road sweeping beneath"></div>
    <div class="star-row" aria-hidden="true">
      <svg style="left:100px"><use href="#star"/></svg>
      <svg style="left:184px"><use href="#star"/></svg>
      <svg style="left:270px"><use href="#star"/></svg>
      <svg style="left:364px"><use href="#star"/></svg>
      <svg style="left:455px"><use href="#star"/></svg>
    </div>
    <div class="brand-name">Harborline</div>
    <div class="tagline-band">
      <svg viewBox="0 0 350 39" preserveAspectRatio="none"><path d="M58 0 H350 V39 H0 Q16 2 58 0 Z"/></svg>
      <span class="tagline">Hotel Rate Strategy Advisors</span>
    </div>
    <p class="website">www.HarborlineRA.com</p>
  </section>
</main>
</body>
</html>
```